Newsletter Ad

I am looking for someone to design an advertisement for a mother's club newsletter. 4" wide X by 5" tall (and 2.5" wide X 5" tall if possible).

I'm a psychotherapist, so want the ad to look professional, but modern. I have a logo with my photo attached that can be incorporated into the design. The colors of my website are turquoise and white. I'd like to keep with that theme...so maybe some turquoise blocking to match the logo font color.

I'm uploading a logo as well as an ad draft with the content I'd like listed in the ad.

```html
<!DOCTYPE html>
<html lang="en">
<head>
<meta charset="utf-8">
<title>Dana Morell, MA, MFT — Newsletter Ad</title>
<link rel="stylesheet" href="https://fonts.googleapis.com/css2?family=Josefin+Sans:wght@300;400&display=swap">
<style>
  :root {
    --turquoise: #41c7c5;
    --turquoise-deep: #2fb3b2;
    --white: #ffffff;
    --ink: #1c1c1c;
    --ink-soft: #333333;
  }
  * { margin: 0; padding: 0; box-sizing: border-box; }
  html, body { width: 1200px; height: 2400px; overflow: hidden; background: var(--white); }
  body { font-family: "Josefin Sans", sans-serif; }

  .ad { position: relative; width: 1200px; height: 2400px; background: var(--white); }

  .header { position: absolute; left: 0; top: 0; width: 1200px; height: 533px; }
  .portrait {
    position: absolute; left: 0; top: 0; width: 341px; height: 533px;
    background: radial-gradient(ellipse at 55% 45%, #b98a6a 0%, #6b4a36 38%, #1a1411 75%, #0b0a09 100%);
  }
  .practitioner-name {
    position: absolute; left: 341px; right: 0; top: 62px;
    text-align: center; color: var(--turquoise-deep);
    font-weight: 300; font-size: 74px; letter-spacing: 1px; line-height: 1;
  }
  .practice-tagline {
    position: absolute; left: 341px; right: 0; top: 318px;
    text-align: center; color: var(--ink-soft);
    font-weight: 300; font-size: 41px; line-height: 66px;
  }

  .specialties {
    position: absolute; left: 0; top: 533px; width: 1200px; height: 1254px;
    background: var(--turquoise);
    list-style: none; text-align: center; color: var(--white);
    padding-top: 138px;
  }
  .specialties li { font-weight: 300; font-size: 74px; line-height: 120px; }

  .contact {
    position: absolute; left: 0; top: 1787px; width: 1200px;
    text-align: center; color: var(--ink);
    font-weight: 300; padding-top: 72px;
  }
  .contact-address { font-size: 54px; line-height: 74px; margin-bottom: 4px; }
  .contact-line { font-size: 49px; line-height: 71px; }

  .footer-band {
    position: absolute; left: 0; top: 2227px; width: 1200px; height: 173px;
    background: var(--turquoise);
  }
  .license {
    position: absolute; right: 40px; top: 55px;
    font-weight: 300; font-size: 44px; color: var(--ink);
  }
</style>
</head>
<body>
  <main class="ad">
    <header class="header">
      <div class="portrait" role="img" aria-label="Portrait photograph of the therapist"></div>
      <h1 class="practitioner-name">DANA MORELL, MA, MFT</h1>
      <p class="practice-tagline">Psychotherapy for Individuals,<br>Couples and Families</p>
    </header>

    <ul class="specialties">
      <li>Parenting</li>
      <li>Depression</li>
      <li>Anxiety</li>
      <li>Life Transitions</li>
      <li>Divorce</li>
      <li>Couples Issues</li>
      <li>Women’s Issues</li>
      <li>Attachment and Neuroscience</li>
    </ul>

    <address class="contact" style="font-style: normal;">
      <p class="contact-address">148 Harbor Lane, Cedar Bay, CA 94000</p>
      <p class="contact-line">www.danamorell.com</p>
      <p class="contact-line">dana@danamorell.com</p>
      <p class="contact-line">555.210.3846</p>
    </address>

    <footer class="footer-band">
      <p class="license">License# MFC48203</p>
    </footer>
  </main>
</body>
</html>
```